Bright Path Flyer Design for Virtual Online Clinic. -5.5 x 8.5 inches (half sheet)

We need a clean, modern flyer design for Bright Path, a new virtual walk-in clinic based in British Columbia. The flyer will be used in libraries, pharmacies, and community centers to help residents easily access primary care through their Bright Path NFC access card.
The flyer will ask a question : NEED A DOCTOR? This should be large and attention grabbing.
The design should clearly feature a Bright Path card image (the access card) as the centerpiece and visually show how patients can use it to book appointments. The tone should feel trustworthy, healthcare-oriented, and community-friendly — clean fonts, clear spacing, and strong readability from a distance.

Side One: This card has the NFC Access Card.
NEED A DOCTOR? (Large Font, Attention Grabbing)
How to Book an Appointment using your Bright Path Card
Step 1: Tap Your Card on Your Phone
Hold your card near the back of your phone.
It will activate automatically — no app needed.
The Bright Path scheduler will open.
Step 2: Schedule Your Appointment
Select your clinical concern.
Choose your time window.
Register (only once).
Confirm your appointment.
Step 3: Relax, we’ll take care of the rest
A doctor will call during your scheduled time.
Once booked, you’ll be able to call our office.
No emails, no texts — just a real person.
It’s that simple.
Side Two:
About Bright Path
Created by Dr. Marcus Ferrigan
Bright Path was founded to make healthcare simple and convenient. Prescription renewals. Common infections. Medical notes. And so much more.
Our doctors can address 120+ health concerns virtually — providing quality care without the waiting room. No waiting rooms. Just real doctors providing real care.
Why Patients Choose Bright Path
Easy access – book and be seen from anywhere in BC.
Effortless booking – tap your Bright Path Card to begin.
Trusted physicians – every visit is with a licensed BC family doctor.
How It Works
Book your visit — choose a time window that fits your day.
Join the queue — you’ll be called when it’s your turn.
Speak directly with your doctor — simple, secure, and stress-free.
Convenient Care for Common Concerns

Additional Details.
Please find the domain to be launched soon. I've attached the NFC card file for review, it is 85.5 mm x 54 mm. The card will be glued to the flyer.
I've attached examples of flyers but they are not the look I am seeking and I am looking for creative solutions.
Thank you!
http://brightpath-example.test/

Adult Patients in British Columbia

Healthcare

• Looking for clean lines, uniform appearance, and high legibility i.e poppins

0054AA
0677BA
7BADD7
CADEEF
E8F1F8

• Need A Doctor?
• Elegant style, not too busy, clear layout.
• Clutter, look cheap - review examples.

```html
<!DOCTYPE html>
<html lang="en">
<head>
<meta charset="utf-8">
<title>Bright Path Flyer – Front and Back</title>
<link href="https://fonts.googleapis.com/css2?family=Poppins:wght@400;600;700;800;900&family=Playfair+Display:ital,wght@1,400&family=Oswald:wght@300&family=Allura&display=swap" rel="stylesheet">
<style>
  :root{
    --stage:#8a8a8a;
    --navy:#2b448f;
    --white:#ffffff;
    --card-white:#f4f6fb;
    --skin-light:#eccab2;
    --skin-deep:#d9a88a;
    --yellow:#ece04a;
    --mint:#8fdcc3;
    --pink:#e6c3dc;
    --green:#3cb98b;
    --ink:#1f2a44;
    --body:#2a2f3a;
    --grey-num:#a9adb6;
  }
  *{margin:0;padding:0;box-sizing:border-box}
  html,body{width:1200px;height:783px;overflow:hidden}
  body{background:var(--stage);font-family:'Poppins',sans-serif;position:relative}

  .side-label{position:absolute;top:26px;color:var(--white);font-weight:700;font-size:19px;letter-spacing:9px;transform:translateX(-50%)}
  .side-label.front{left:304px}
  .side-label.back{left:876px}

  .flyer{position:absolute;top:55px;width:526px;height:681px;overflow:hidden}
  .flyer.front{left:53px;background:var(--navy)}
  .flyer.back{left:620px;background:var(--white)}
  .edge-shape{position:absolute;inset:0;width:526px;height:681px}

  .brand-name{position:absolute;font-weight:600}
  .front .brand-name{left:57px;top:18px;font-size:22px;color:var(--white)}
  .back .brand-name{left:32px;top:38px;font-size:26px;color:var(--navy)}

  /* front */
  .question{position:absolute;left:57px;top:46px;font-weight:900;font-size:31px;line-height:36px;color:var(--white);letter-spacing:.3px}
  .accent-bar{position:absolute;left:0;top:97px;width:14px;height:46px;background:var(--yellow)}
  .headline{position:absolute;left:57px;top:94px;font-weight:800;font-size:23.5px;line-height:28px;color:var(--white);letter-spacing:-.2px}
  .headline .hi{color:var(--yellow)}
  .card-photo{position:absolute;left:121px;top:170px;width:217px;height:126px;border-radius:6px;background:var(--card-white)}
  .hand-photo{position:absolute;left:272px;top:262px;width:112px;height:146px;border-radius:40px 20px 30px 50px;
    background:linear-gradient(160deg,var(--skin-light),var(--skin-deep))}
  .step{position:absolute;left:57px}
  .step-badge{display:inline-block;background:var(--pink);color:var(--navy);font-weight:700;font-size:14px;line-height:22px;padding:0 12px 0 6px;border-radius:0 11px 11px 0}
  .step-title{color:var(--mint);font-weight:700;font-size:17px;line-height:20.5px;margin-top:4px}
  .ticks{list-style:none;margin-top:5px;color:var(--white);font-size:8px;line-height:11px}
  .ticks li{position:relative;padding-left:10px}
  .ticks li::before{content:"";position:absolute;left:1px;top:2px;width:3px;height:6px;border:solid var(--yellow);border-width:0 1.6px 1.6px 0;transform:rotate(40deg)}
  .ticks.two-col{display:grid;grid-template-columns:127px auto}
  .step-1{top:290px}
  .step-2{top:419px}
  .step-3{top:513px}
  .tagline-front{position:absolute;left:57px;top:614px;font-family:'Allura',cursive;font-size:37px;color:var(--white)}

  /* back */
  .section-title{position:absolute;left:32px;color:var(--navy);font-weight:700;font-size:20px;line-height:23px}
  .about-title{top:96px}
  .byline{position:absolute;left:32px;top:130px;font-family:'Playfair Display',serif;font-style:italic;font-size:11px;color:var(--navy)}
  .about-body{position:absolute;left:32px;top:146px;font-size:10px;line-height:13.4px;color:var(--body)}
  .about-quote{position:absolute;left:32px;top:197px;width:340px;font-family:'Playfair Display',serif;font-style:italic;font-size:12.3px;line-height:15.6px;color:var(--navy)}
  .why-title{top:272px;font-size:19px;line-height:23px}
  .why-title .green{color:var(--green)}
  .reason{position:absolute;left:32px;display:flex;gap:5px}
  .reason-icon{width:42px;height:42px;flex:none}
  .reason h3{color:var(--green);font-weight:600;font-size:14px;line-height:16px}
  .reason p{font-size:9.3px;line-height:12.2px;color:var(--body);margin-top:2px}
  .reason-1{top:331px}
  .reason-2{top:386px}
  .reason-3{top:438px}
  .how-title{top:502px;font-size:19px}
  .how-step{position:absolute;display:flex;gap:5px}
  .how-num{font-family:'Oswald',sans-serif;font-weight:300;font-size:27px;line-height:30px;color:var(--grey-num);padding-right:5px;border-right:1px dashed var(--green)}
  .how-step h4{color:var(--navy);font-weight:600;font-size:12px;line-height:14px}
  .how-step p{font-size:8.5px;line-height:11.5px;color:var(--body);margin-top:2px}
  .how-1{left:32px;top:530px}
  .how-2{left:174px;top:530px}
  .how-3{left:32px;top:577px}
  .tagline-back{position:absolute;left:32px;top:624px;font-family:'Allura',cursive;font-size:25px;color:var(--ink);white-space:nowrap}
</style>
</head>
<body>
  <div class="side-label front">FRONT</div>
  <div class="side-label back">BACK</div>

  <section class="flyer front">
    <svg class="edge-shape" viewBox="0 0 526 681" aria-hidden="true">
      <path d="M487 0 H526 V681 H350 C420 600 460 520 440 430 C420 350 470 260 487 0 Z" fill="var(--white)"/>
    </svg>
    <div class="brand-name">Bright Path</div>
    <p class="question">NEED A DOCTOR?</p>
    <div class="accent-bar"></div>
    <h1 class="headline"><span class="hi">How to Book an Appointment</span><br>using your Bright Path Card</h1>
    <div class="hand-photo" role="img" aria-label="Photo of a hand holding the access card"></div>
    <div class="card-photo" role="img" aria-label="Bright Path NFC access card with tap-to-book mark"></div>

    <div class="step step-1">
      <span class="step-badge">STEP 1</span>
      <h2 class="step-title">Tap Your Card on<br>Your Phone</h2>
      <ul class="ticks">
        <li>Hold your card near the back of your phone.</li>
        <li>It will activate automatically — no app needed.</li>
        <li>The Bright Path scheduler will open.</li>
      </ul>
    </div>
    <div class="step step-2">
      <span class="step-badge">STEP 2</span>
      <h2 class="step-title">Schedule Your Appointment</h2>
      <ul class="ticks two-col">
        <li>Select your clinical concern.</li>
        <li>Register (only once).</li>
        <li>Choose your time window.</li>
        <li>Confirm your appointment.</li>
      </ul>
    </div>
    <div class="step step-3">
      <span class="step-badge">STEP 3</span>
      <h2 class="step-title">Relax, we’ll take care of the rest</h2>
      <ul class="ticks">
        <li>A doctor will call during your scheduled time.</li>
        <li>Once booked, you’ll be able to call our office.</li>
        <li>No emails, no texts — just a real person.</li>
      </ul>
    </div>
    <p class="tagline-front">its that Simple.</p>
  </section>

  <section class="flyer back">
    <svg class="edge-shape" viewBox="0 0 526 681" aria-hidden="true">
      <path d="M486 0 H526 V681 H350 C420 600 460 520 450 420 C440 320 470 220 486 0 Z" fill="var(--navy)"/>
    </svg>
    <div class="brand-name">Bright Path</div>
    <h2 class="section-title about-title">About Bright Path</h2>
    <p class="byline">Created by Dr. Marcus Ferrigan</p>
    <p class="about-body">Bright Path was founded to make healthcare simple and convenient.<br>Prescription renewals. Common infections. Medical notes.<br>And so much more.</p>
    <p class="about-quote">Our doctors can address 120+ health concerns virtually — providing quality care without the waiting room. No waiting rooms. Just real doctors providing real care.</p>

    <h2 class="section-title why-title">Why Patients Choose<br><span class="green">Bright Path</span></h2>
    <div class="reason reason-1">
      <svg class="reason-icon" viewBox="0 0 42 42" aria-hidden="true"><circle cx="21" cy="21" r="21" fill="var(--green)"/><rect x="11" y="12" width="20" height="14" rx="2" fill="none" stroke="#fff" stroke-width="1.5"/><path d="M15 30h12M21 26v4" stroke="#fff" stroke-width="1.5"/></svg>
      <div><h3>Easy access</h3><p>Book and be seen from<br>anywhere in BC.</p></div>
    </div>
    <div class="reason reason-2">
      <svg class="reason-icon" viewBox="0 0 42 42" aria-hidden="true"><circle cx="21" cy="21" r="21" fill="var(--green)"/><rect x="9" y="11" width="24" height="9" rx="2" fill="none" stroke="#fff" stroke-width="1.4"/><path d="M19 33v-9a2 2 0 0 1 4 0v5h3a2 2 0 0 1 2 2v2" fill="none" stroke="#fff" stroke-width="1.4"/></svg>
      <div><h3>Effortless booking</h3><p>Tap your Bright Path<br>Card to begin.</p></div>
    </div>
    <div class="reason reason-3">
      <svg class="reason-icon" viewBox="0 0 42 42" aria-hidden="true"><circle cx="21" cy="21" r="21" fill="var(--green)"/><circle cx="21" cy="13" r="4" fill="none" stroke="#fff" stroke-width="1.4"/><path d="M13 31a8 8 0 0 1 16 0" fill="none" stroke="#fff" stroke-width="1.4"/><path d="M19 13l1.5 1.5 3-3" fill="none" stroke="#fff" stroke-width="1.2"/></svg>
      <div><h3>Trusted physicians</h3><p>Every visit is with a licensed BC<br>family doctor.</p></div>
    </div>

    <h2 class="section-title how-title">How It Works</h2>
    <div class="how-step how-1"><span class="how-num">01</span><div><h4>Book your visit</h4><p>Choose a time window<br>that fits your day.</p></div></div>
    <div class="how-step how-2"><span class="how-num">02</span><div><h4>Join the queue</h4><p>You’ll be called when it’s<br>your turn.</p></div></div>
    <div class="how-step how-3"><span class="how-num">03</span><div><h4>Speak directly with your doctor</h4><p>simple, secure, and stress-free.</p></div></div>

    <p class="tagline-back">Convenient Care for Common Concerns</p>
  </section>
</body>
</html>
```